Email Preference Page Design

We are looking for a 2 page design for our users to edit their email preferences and submit friend referrals. You can find the fuctionality, content and text here:

https://brightcart.examplemail.net/app/linkClick/7281/5c9a1b3e8d04f2aa/20583941/7f3d9e2b1a6c4058

* the shipping and billing address might be different so you need to show the billing if the "same as shipping" box is not checked. It can auto-hide like the page above shows if that fits your design.

* when the "unsubscribe from all email lists" box is selected, all the other checkbox options will hide as in the example page. We need you to show us what the site will look like with and without that checkbox selected.

We want to match these two pages to the general feel of these website pages:

www.brightcart.com
and
free.brightcart.com

The page should be very clean and tight. Project is for design only but must be able to be implemented in html showing button and checkbox states. Technically this must be two pages for our system - one for all the user info and one for individual email referrals (see example above).

Target Market(s)

video professionals

Industry/Entity Type

Shipping

Requirements
Must have
• our logo (see numerous versions attached)
well designed header
well designed sections
clean editable text
tight layout
html friendly
easy to understand
2 pages
Nice to have
• custom checkboxes and radio buttons

```html
<!DOCTYPE html>
<html lang="en">
<head>
<meta charset="utf-8">
<title>Spread the Love – Brightcart</title>
<link rel="stylesheet" href="https://fonts.googleapis.com/css2?family=Jura:wght@500&family=Open+Sans:wght@400;600&display=swap">
<style>
  :root {
    --navy: #1c2f3f;
    --social-blue: #4a66ad;
    --social-blue-dark: #3a5296;
    --orange-top: #fba23a;
    --orange-bottom: #ee7d06;
    --orange-edge: #d86f04;
    --text: #1f2a33;
    --field-border: #d2d6da;
    --placeholder: #7d8790;
    --white: #ffffff;
    --tab-shadow: #e3e6e9;
    --icon-fill: #e4e8f1;
  }
  * { box-sizing: border-box; margin: 0; padding: 0; }
  html, body { width: 857px; height: 1200px; overflow: hidden; background: var(--white); }
  body { position: relative; font-family: "Open Sans", Arial, sans-serif; color: var(--text); }

  .top-bar { position: absolute; left: 0; top: 0; width: 857px; height: 13px; background: var(--navy); }
  .brand-tab { position: absolute; left: 200px; top: 0; width: 457px; height: 122px; }
  .brand-name {
    position: absolute; left: 206px; top: 22px; width: 445px; height: 60px;
    display: flex; align-items: center; justify-content: center; gap: 12px;
    color: var(--white); font-size: 48px; font-weight: 400; letter-spacing: 0.5px;
  }
  .brand-dot { width: 26px; height: 26px; border-radius: 50%; background: var(--orange-bottom); }

  .love-icon {
    position: absolute; left: 383px; top: 160px; width: 91px; height: 85px;
    border-radius: 12px; background: var(--icon-fill);
  }

  .headline {
    position: absolute; left: 153px; top: 284px; width: 551px;
    text-align: center; font-family: "Jura", "Arial Narrow", sans-serif; font-weight: 500;
    font-size: 50px; line-height: 46px; color: var(--navy); letter-spacing: 0;
    padding-bottom: 4px; border-bottom: 2px solid var(--navy);
  }

  .intro { position: absolute; left: 40px; top: 362px; width: 777px; text-align: center; font-size: 14.5px; line-height: 20.6px; }
  .intro p + p { margin-top: 20.6px; }

  .rewards { position: absolute; left: 44px; top: 579px; width: 769px; height: 236px; background: var(--navy); border-radius: 2px; }
  .rewards-share {
    position: absolute; left: 0; top: 0; width: 165px; height: 236px; background: var(--social-blue);
    border-radius: 2px 0 0 2px; display: flex; flex-direction: column; align-items: center; color: var(--white);
  }
  .share-circle { margin-top: 45px; width: 58px; height: 58px; border-radius: 50%; border: 4px solid var(--white); }
  .share-label { margin-top: 6px; font-size: 24px; line-height: 29px; font-weight: 600; text-align: center; }
  .rewards-or {
    position: absolute; left: 148px; top: 79px; width: 34px; height: 34px; border-radius: 50%;
    background: var(--social-blue); color: var(--white); font-size: 14px; font-weight: 600;
    display: flex; align-items: center; justify-content: center;
  }
  .reward-list { position: absolute; left: 203px; top: 56px; color: var(--white); font-size: 15.5px; line-height: 19px; }
  .reward-row { display: flex; }
  .reward-row .step { width: 229px; }
  .reward-row .equals { width: 37px; }
  .reward-total { margin-top: 16px; width: 540px; }

  .field {
    position: absolute; top: 846px; height: 37px; border: 2px solid var(--field-border); background: var(--white);
    font-family: "Open Sans", Arial, sans-serif; font-size: 14.5px; color: var(--text); padding: 0 15px;
  }
  .field::placeholder { color: var(--placeholder); }
  .field-name { left: 51px; width: 376px; }
  .field-email { left: 433px; width: 376px; }

  .btn {
    position: absolute; display: flex; align-items: center; justify-content: center; gap: 12px;
    color: var(--white); font-family: "Open Sans", Arial, sans-serif; font-weight: 600; border-radius: 3px; cursor: pointer;
  }
  .btn-share {
    left: 229px; top: 910px; width: 376px; height: 61px; font-size: 26px;
    background: linear-gradient(var(--social-blue), var(--social-blue-dark)); border: 1px solid #2e4483;
  }
  .btn-share .btn-mark { width: 16px; height: 16px; border-radius: 50%; background: var(--white); }
  .btn-invite {
    left: 293px; top: 1028px; width: 272px; height: 62px; font-size: 26px;
    background: linear-gradient(var(--orange-top), var(--orange-bottom)); border: 1px solid var(--orange-edge);
    text-shadow: 0 1px 1px rgba(0,0,0,0.25);
  }
  .btn-share:hover { background: var(--social-blue-dark); }
  .btn-invite:hover { background: var(--orange-bottom); }

  .choice-or {
    position: absolute; left: 415px; top: 990px; width: 26px; height: 26px; border-radius: 50%;
    background: var(--navy); color: var(--white); font-size: 11px; font-weight: 600;
    display: flex; align-items: center; justify-content: center;
  }

  .site-footer {
    position: absolute; left: 0; top: 1147px; width: 857px; height: 53px; background: var(--navy);
    color: var(--white); font-size: 14.5px; display: flex; align-items: center; justify-content: center;
  }
</style>
</head>
<body>
  <div class="top-bar"></div>
  <svg class="brand-tab" viewBox="0 0 457 122" aria-hidden="true">
    <path d="M0 13 L0 103 Q228 130 457 103 L457 13 Z" fill="var(--tab-shadow)"/>
    <path d="M6 0 L6 96 Q228 122 451 96 L451 0 Z" fill="var(--navy)"/>
  </svg>
  <div class="brand-name"><span class="brand-dot"></span>brightcart</div>

  <div class="love-icon" role="img" aria-label="Heart-shaped handshake icon"></div>

  <h1 class="headline">SPREAD THE LOVE!</h1>

  <div class="intro">
    <p>We've just emailed your code to unlock all the free and exclusive videos at free.brightcart.com.<br>
    Help us spread the love about these free loops and we will give you private access to 10 additional<br>
    free motion loops!</p>
    <p>To receive download links to these bonus videos, please share us on Sharebook using the button<br>
    below or enter a friend's name and email address. All they have to do is open the email for your to<br>
    receive the bonus freebies - they don't even have to subscribe. Your friends will surely thank you for<br>
    the invitation to download all our free loops!</p>
  </div>

  <section class="rewards">
    <div class="rewards-share">
      <span class="share-circle"></span>
      <span class="share-label">Sharebook<br>Share</span>
    </div>
    <span class="rewards-or">or</span>
    <div class="reward-list">
      <div class="reward-row"><span class="step">Enter friend #1 email address</span><span class="equals">=</span><span>earn 2 bonus motion loops</span></div>
      <div class="reward-row"><span class="step">Enter friend #2 email address</span><span class="equals">=</span><span>earn 3 additional bonus motion loops</span></div>
      <div class="reward-row"><span class="step">Enter friend #3 email address</span><span class="equals">=</span><span>earn 5 additional bonus motion loops</span></div>
      <p class="reward-total">That's 10 additional free hd motion loops just for spreading the love about our new free downloads website free.brightcart.com!</p>
    </div>
  </section>

  <input class="field field-name" type="text" placeholder="Friend's First Name *">
  <input class="field field-email" type="email" placeholder="Friend's Email Address *">

  <button class="btn btn-share" type="button"><span class="btn-mark"></span>Share on Sharebook</button>
  <span class="choice-or">or</span>
  <button class="btn btn-invite" type="submit">Send the Invite</button>

  <footer class="site-footer">All right reserved copyright 2013 - Brightcart</footer>
</body>
</html>
```